Manufacturing company needs new business card.

I need a unique Business Card that will truly stand out. Nothing too busy. Simple is good, right? Not looking for a standard design either. No cookie cutter layout. I am just looking for something interesting and a bit different. Does't have to completely off the wall crazy, just not your run of the mill business card. Clean and modern with a touch of industrial.

Target Market(s)

Air conditioning industry, Architects, builders.

Industry/Entity Type

Business

Contact Information for Business Card

Details to be included on card are:

Peter Vance
Managing Director

T: 1300 847 519
M: 0428 593 174
W: www.brenvaleworks.com.au
E: peter.vance@brenvaleworks.com.au
A: 58 Harwick Lane, Sydney NSW 2000

Font styles to use
Sans Serif

Colors
0355a3
848484
fbfbfb

Requirements
Must have
• Card design must be landscape.

```html
<!DOCTYPE html>
<html lang="en">
<head>
<meta charset="utf-8">
<title>Brenvale Works – Business Card</title>
<link href="https://fonts.googleapis.com/css2?family=Open+Sans:wght@400;600&display=swap" rel="stylesheet">
<style>
  :root {
    --brand-blue: #1f4fa3;
    --brand-blue-deep: #2453a6;
    --brand-blue-soft: #3563b2;
    --brand-grey: #7c7c7c;
    --text-grey: #666666;
    --card-white: #fbfbfb;
    --stage: #e6e6e6;
  }
  * { margin: 0; padding: 0; box-sizing: border-box; }
  html, body {
    width: 1200px; height: 1000px; overflow: hidden;
    background: var(--stage);
    font-family: "Open Sans", Arial, sans-serif;
  }
  .stage { position: relative; width: 1200px; height: 1000px; }
  .card {
    position: absolute; left: 266px; width: 666px; height: 397px;
    box-shadow: 0 4px 14px rgba(0,0,0,0.18);
  }
  .card--front { top: 74px; background: var(--card-white); }
  .card--back { top: 534px; background: var(--brand-blue-deep); overflow: hidden; }

  .brand-name {
    position: absolute; left: 32px; top: 62px;
    font-weight: 600; font-size: 30px; letter-spacing: -0.3px;
    color: var(--brand-blue);
  }
  .brand-square {
    position: absolute; left: 516px; top: 34px;
    width: 115px; height: 118px; border-radius: 8px;
    background: var(--brand-blue);
  }

  .person { position: absolute; left: 32px; top: 196px; }
  .person__name { font-weight: 600; font-size: 24px; color: var(--brand-grey); line-height: 1.2; }
  .person__role { font-size: 16px; color: var(--brand-blue); line-height: 1.3; }
  .role-rule {
    position: absolute; left: 188px; top: 236px; width: 446px; height: 2px;
    background: var(--brand-blue);
  }

  .contacts { position: absolute; left: 32px; top: 262px; list-style: none; }
  .contacts li {
    display: flex; align-items: center; height: 25.5px;
    font-size: 16px; color: var(--text-grey);
  }
  .contacts svg { width: 16px; height: 16px; margin-right: 8px; fill: var(--brand-blue); }

  .address {
    position: absolute; right: 32px; top: 288px; text-align: right;
    font-size: 16px; line-height: 24px; color: var(--text-grey); font-style: normal;
  }

  .back-pattern {
    position: absolute; inset: 0;
    background: linear-gradient(180deg, var(--brand-blue-soft) 0%, var(--brand-blue-deep) 100%);
    opacity: 0.55;
  }
  .back-brand {
    position: absolute; left: 228px; top: 250px;
    display: flex; align-items: center; gap: 24px;
  }
  .back-brand__square { width: 55px; height: 55px; border-radius: 5px; background: #ffffff; }
  .back-brand__name { font-weight: 600; font-size: 30px; color: #ffffff; letter-spacing: -0.3px; }
</style>
</head>
<body>
<main class="stage">
  <section class="card card--front" aria-label="Business card front">
    <div class="brand-name">Brenvale Works</div>
    <div class="brand-square" aria-hidden="true"></div>

    <div class="person">
      <div class="person__name">Peter Vance</div>
      <div class="person__role">Managing Director</div>
    </div>
    <div class="role-rule"></div>

    <ul class="contacts">
      <li>
        <svg viewBox="0 0 16 16" aria-hidden="true"><path d="M4 1h8a1 1 0 0 1 1 1v12a1 1 0 0 1-1 1H4a1 1 0 0 1-1-1V2a1 1 0 0 1 1-1zm1 2v9h6V3H5zm3 10a.8.8 0 1 0 0 .01z"/></svg>
        1300 847 519
      </li>
      <li>
        <svg viewBox="0 0 16 16" aria-hidden="true"><path d="M1 6c0-2 3-3 7-3s7 1 7 3v1h-3V5.5C11 5 9.5 5 8 5s-3 0-4 .5V7H1zM3 8h10l1.5 5H1.5zm5 1.5a1.5 1.5 0 1 0 0 3 1.5 1.5 0 0 0 0-3z"/></svg>
        0428 593 174
      </li>
      <li>
        <svg viewBox="0 0 16 16" aria-hidden="true"><path d="M1 3h14v10H1zm1.5 1.2V5l5.5 4 5.5-4v-.8z"/></svg>
        peter.vance@brenvaleworks.com.au
      </li>
      <li>
        <svg viewBox="0 0 16 16" aria-hidden="true"><path d="M1 2h14v9H1zm1.5 1.5v6h11v-6zM6 12h4v1.5h2V15H4v-1.5h2z"/></svg>
        www.brenvaleworks.com.au
      </li>
    </ul>

    <address class="address">58 Harwick Lane, Sydney<br>NSW 2000</address>
  </section>

  <section class="card card--back" aria-label="Business card back">
    <div class="back-pattern" role="img" aria-label="Faint repeating brand pattern in tonal blue"></div>
    <div class="back-brand">
      <div class="back-brand__square" aria-hidden="true"></div>
      <div class="back-brand__name">Brenvale Works</div>
    </div>
  </section>
</main>
</body>
</html>
```